I need to add on from our previous project a couple extra signs

We need to create two signs from your original desgin with a arrow saying 600M on the left.
also another sign drawn up similar to the one attached but also adding in there that the containers are 20ft/40ft and we have caravan, car and boat storage.
also add on the sign something for " sign online or call the number to rent space"

```html
<!DOCTYPE html>
<html lang="en">
<head>
<meta charset="utf-8">
<title>Keystone Self Storage – Roadside Signs</title>
<link href="https://fonts.googleapis.com/css2?family=Poppins:wght@600;700;800&display=swap" rel="stylesheet">
<style>
:root{
  --red:#d0202a;
  --ink:#262223;
  --white:#ffffff;
  --backdrop:#dcdcdc;
}
*{box-sizing:border-box;margin:0;padding:0}
html,body{width:1200px;height:850px;overflow:hidden}
body{background:var(--backdrop);font-family:"Poppins",Arial,sans-serif;position:relative;color:var(--ink)}
.sign{position:absolute;background:var(--white);box-shadow:0 3px 8px rgba(0,0,0,.25);overflow:hidden}
.sign--direction{left:94px;top:90px;width:1012px;height:296px}
.sign--info{left:96px;top:442px;width:1011px;height:295px}
.brand{position:absolute;display:flex;align-items:center}
.brand__dot{border-radius:50%;background:var(--red);flex:none}
.brand__text{display:flex;flex-direction:column}
.brand__name{font-weight:800;color:var(--ink);line-height:1;letter-spacing:.5px}
.brand__web{font-weight:600;color:var(--ink)}
.brand__phone{font-weight:800;color:var(--red);letter-spacing:2px}
.sign--direction .brand{left:345px;top:30px}
.sign--direction .brand__dot{width:96px;height:96px;margin-right:14px}
.sign--direction .brand__name{font-size:31px}
.sign--direction .brand__web{font-size:13px;margin-top:4px}
.sign--direction .brand__phone{font-size:17px;line-height:1.1}
.band{position:absolute;left:0;right:0;bottom:0;background:var(--ink)}
.sign--direction .band{top:148px;display:flex;align-items:center;justify-content:space-between;padding:0 30px 0 28px}
.chevrons{width:108px;height:80px;flex:none}
.direction__text{color:var(--white);font-weight:800;font-size:74px;letter-spacing:1px;line-height:1;white-space:nowrap}
.sign--info .brand{left:30px;top:32px;align-items:flex-start}
.sign--info .brand__dot{width:70px;height:70px;margin-right:12px}
.sign--info .brand__name{font-size:23px}
.sign--info .brand__web{font-size:10px;margin-top:3px}
.sign--info .brand__phone{font-size:13px;line-height:1.1}
.rent{position:absolute;left:30px;top:122px;font-weight:800;font-size:21px;line-height:25px;color:var(--ink)}
.rent__accent{color:var(--red)}
.sizes{position:absolute;left:448px;top:30px;width:530px;height:40px;background:var(--ink);border-radius:7px;display:flex;align-items:center;padding-left:14px}
.sizes__icon{width:50px;height:28px;margin-right:30px}
.sizes__text{color:var(--white);font-weight:700;font-size:29px;line-height:1;white-space:nowrap}
.offer{position:absolute;font-weight:700;font-size:21px;line-height:25px;color:var(--ink);text-align:center;white-space:nowrap}
.offer--lead{left:463px;top:95px;text-align:left}
.offer__icon{display:block;margin:0 auto 6px;height:32px}
.offer--caravan{left:548px;top:82px;width:120px}
.offer--car{left:694px;top:82px;width:80px}
.offer--boat{left:804px;top:82px;width:175px}
.sign--info .band{top:176px}
.why__title{position:absolute;left:30px;top:16px;color:var(--red);font-weight:800;font-size:38px;line-height:1}
.why__text{position:absolute;left:28px;top:64px;color:var(--white);font-weight:700;font-size:26px;line-height:1;white-space:nowrap}
.feature{position:absolute;top:9px;width:88px;text-align:center}
.feature__tile{width:59px;height:59px;margin:0 auto;background:var(--red);border-radius:2px;display:flex;align-items:center;justify-content:center}
.feature__label{color:var(--white);font-weight:700;font-size:19px;margin-top:12px;line-height:1}
.feature--vermin{left:590px}.feature--insect{left:677px}.feature--water{left:764px}.feature--dust{left:850px}
</style>
</head>
<body>

<section class="sign sign--direction">
  <div class="brand">
    <span class="brand__dot"></span>
    <div class="brand__text">
      <span class="brand__name">KEYSTONE<br>SELF STORAGE</span>
      <span class="brand__web">www.keystonestorage.com.au</span>
      <span class="brand__phone">(03) 5550 0142</span>
    </div>
  </div>
  <div class="band">
    <svg class="chevrons" viewBox="0 0 108 80" aria-hidden="true"><g fill="var(--red)"><polygon points="0,0 26,0 58,40 26,80 0,80 32,40"/><polygon points="50,0 76,0 108,40 76,80 50,80 82,40"/></g></svg>
    <span class="direction__text">600M ON THE LEFT</span>
    <svg class="chevrons" viewBox="0 0 108 80" aria-hidden="true"><g fill="var(--red)"><polygon points="0,0 26,0 58,40 26,80 0,80 32,40"/><polygon points="50,0 76,0 108,40 76,80 50,80 82,40"/></g></svg>
  </div>
</section>

<section class="sign sign--info">
  <div class="brand">
    <span class="brand__dot"></span>
    <div class="brand__text">
      <span class="brand__name">KEYSTONE<br>SELF STORAGE</span>
      <span class="brand__web">www.keystonestorage.com.au</span>
      <span class="brand__phone">(03) 5550 0142</span>
    </div>
  </div>
  <p class="rent">SIGN ONLINE OR<br>CALL THE NUMBER TO <span class="rent__accent">RENT SPACE</span></p>

  <div class="sizes">
    <svg class="sizes__icon" viewBox="0 0 50 28" aria-hidden="true"><g fill="none" stroke="var(--red)" stroke-width="2"><rect x="2" y="2" width="46" height="24"/><path d="M10 6v16M16 6v16M22 6v16M28 6v16M34 6v16M40 6v16"/></g></svg>
    <span class="sizes__text">CONTAINERS ARE 20FT/40FT</span>
  </div>

  <p class="offer offer--lead">WE<br>HAVE</p>
  <div class="offer offer--caravan">
    <svg class="offer__icon" viewBox="0 0 76 32" width="76" aria-hidden="true"><rect x="14" y="2" width="60" height="24" rx="5" fill="var(--red)"/><rect x="0" y="23" width="16" height="3" fill="var(--red)"/><circle cx="40" cy="27" r="5" fill="var(--red)" stroke="#fff" stroke-width="2"/></svg>
    CARAVAN
  </div>
  <div class="offer offer--car">
    <svg class="offer__icon" viewBox="0 0 48 36" width="46" aria-hidden="true"><path d="M10 4h28l5 12h3v12h-6v6h-6v-6H14v6H8v-6H2V16h3z" fill="var(--red)"/><path d="M12 8h24l3 8H9z" fill="#fff"/><circle cx="11" cy="22" r="3" fill="#fff"/><circle cx="37" cy="22" r="3" fill="#fff"/></svg>
    CAR
  </div>
  <div class="offer offer--boat">
    <svg class="offer__icon" viewBox="0 0 84 32" width="84" aria-hidden="true"><path d="M0 20h84l-10 12H8z" fill="var(--red)"/><path d="M22 20l8-10h26l12 10z" fill="var(--red)"/></svg>
    BOAT STORAGE
  </div>

  <div class="band">
    <h2 class="why__title">WHY CHOOSE US?</h2>
    <p class="why__text">SHIPPING CONTAINERS ARE FREE FROM</p>
    <div class="feature feature--vermin">
      <div class="feature__tile" role="img" aria-label="Vermin icon"></div>
      <p class="feature__label">VERMIN</p>
    </div>
    <div class="feature feature--insect">
      <div class="feature__tile" role="img" aria-label="Insect icon"></div>
      <p class="feature__label">INSECT</p>
    </div>
    <div class="feature feature--water">
      <div class="feature__tile"><svg viewBox="0 0 30 40" width="30" height="40" aria-hidden="true"><path d="M15 2C15 2 3 18 3 26a12 12 0 0 0 24 0C27 18 15 2 15 2z" fill="#fff"/></svg></div>
      <p class="feature__label">WATER</p>
    </div>
    <div class="feature feature--dust">
      <div class="feature__tile" role="img" aria-label="Dust cloud icon"></div>
      <p class="feature__label">DUST</p>
    </div>
  </div>
</section>

</body>
</html>
```